Real Estate Managemene Company Needs Business Card Design

We have a logo design and just need business cards made now for our business. Please use PDF logo # 3.

Card with Information to be attached shortly.

The card is used for a real estate management company. We will need to add four other employees and their cards.

Industry/Entity Type

Real Estate

Contact Information for Business Card

Tariq Hamdan
President
3187 Thornwick Avenue
Suite C
Glendale Heights, IL 60152
Phone 630.417.2286
Fax 630.417.2287
Cell 630.473.8062
vantorp@mailbreeze.net

Once design is approved we will have four other employees
Omar Hamdan
Operations Manager

Nadia Hamdan
Administrative Manager

Faz Hamdan
Principal

We would need to take out the cell # 630.473.8062 out for the remaining three cards.

Requirements
Must have
• Please use logo attached

```html
<!DOCTYPE html>
<html lang="en">
<head>
<meta charset="utf-8">
<title>Maple Crest Property Management – Business Card</title>
<link href="https://fonts.googleapis.com/css2?family=Source+Sans+3:wght@400;600;700;800&display=swap" rel="stylesheet">
<style>
  :root {
    --backdrop: #3a3a3c;
    --card: #ffffff;
    --brand-red: #d9232e;
    --ink-grey: #5b5b5d;
    --soft-grey: #7a7a7c;
    --mark-grey: #7d7e80;
  }
  * { box-sizing: border-box; margin: 0; padding: 0; }
  html, body {
    width: 1200px; height: 800px; overflow: hidden;
    background: var(--backdrop);
    font-family: "Source Sans 3", "Source Sans Pro", Arial, sans-serif;
  }
  .business-card {
    position: absolute; left: 180px; top: 160px;
    width: 840px; height: 480px;
    background: var(--card);
    border-bottom: 16px solid var(--brand-red);
    box-shadow: 0 10px 30px rgba(0,0,0,.35);
  }
  .brand {
    position: absolute; left: 70px; top: 170px;
    display: flex; align-items: center; gap: 16px;
  }
  .brand-square { width: 58px; height: 58px; background: var(--mark-grey); flex: none; }
  .brand-name {
    color: var(--brand-red); font-weight: 800; font-size: 27px;
    line-height: 1.05; text-transform: uppercase; letter-spacing: .2px;
    width: 250px;
  }
  .contact-block { position: absolute; left: 450px; top: 62px; color: var(--ink-grey); }
  .person-name {
    color: var(--brand-red); font-weight: 700; font-size: 42px;
    text-transform: uppercase; line-height: 1;
  }
  .person-title { font-size: 30px; line-height: 1.1; margin-bottom: 14px; color: var(--ink-grey); }
  .cell-number { font-size: 22px; margin-bottom: 12px; }
  .address { font-size: 19px; line-height: 1.35; color: var(--soft-grey); }
  .detail-row {
    position: absolute; left: 70px; right: 50px; top: 386px;
    display: flex; justify-content: space-between; align-items: center;
    color: var(--ink-grey); font-size: 22px;
  }
  .detail { display: flex; align-items: center; gap: 12px; }
  .detail svg { width: 24px; height: 20px; fill: var(--brand-red); flex: none; }
</style>
</head>
<body>
  <article class="business-card">
    <div class="brand">
      <div class="brand-square"></div>
      <div class="brand-name">Maple Crest Property Management</div>
    </div>

    <div class="contact-block">
      <h1 class="person-name">Tariq Hamdan</h1>
      <p class="person-title">President</p>
      <p class="cell-number">630.473.8062</p>
      <p class="address">3187 Thornwick Avenue Suite C,<br>Glendale Heights, IL 60152</p>
    </div>

    <div class="detail-row">
      <div class="detail">
        <svg viewBox="0 0 24 20" aria-label="Fax"><rect x="6" y="0" width="12" height="6"/><rect x="0" y="6" width="24" height="10" rx="2"/><rect x="6" y="13" width="12" height="7" fill="#fff" stroke="#d9232e" stroke-width="2"/></svg>
        <span>630.417.2287</span>
      </div>
      <div class="detail">
        <svg viewBox="0 0 24 20" aria-label="Email"><rect x="0" y="2" width="24" height="16"/><path d="M0 2 L12 11 L24 2" fill="none" stroke="#fff" stroke-width="2"/></svg>
        <span>vantorp@mailbreeze.net</span>
      </div>
      <div class="detail">
        <svg viewBox="0 0 24 20" aria-label="Phone"><path d="M2 7 C2 3 22 3 22 7 L22 9 L17 9 L17 6 L7 6 L7 9 L2 9 Z"/><path d="M6 10 L18 10 L21 18 L3 18 Z"/><circle cx="12" cy="14" r="2.5" fill="#fff"/></svg>
        <span>630.417.2286</span>
      </div>
    </div>
  </article>
</body>
</html>
```